Mobil Battery Sales and Instalation

We are a automotive roadside svc company. I am looking to focus on battery sales and instalation We offer tire changes, lockuot, jump starts fuel delivry and battery sales This design should be battery sales and instalation focused My company name is. Harbor Lane Svcs. 909-512-7364 call or text Hours 7am to 9pm. Free service call and instalation with purchase of new battery. Free testing Free battery disposal Colors we like are black and orange or red and black

Target Market(s)

Automotive, RV, Comerical truck, motorcycle and boat

Industry/Entity Type

Automotive

Requirements
Must have
• Pic of battery
• Mobil battery service.
Nice to have
• I want people to see this card and know its a mobil service for battery sales and installation. But can see we offer other services.
• Use my company name but i dont want that to be the standout. (Tuck it in somewhere).
Should not have
• No pictures of any trucks cars etc.
• we do not tow!

```html
<!DOCTYPE html>
<html lang="en">
<head>
<meta charset="utf-8">
<title>Harbor Lane Svcs – Battery Postcard</title>
<link rel="stylesheet" href="https://fonts.googleapis.com/css2?family=Oswald:wght@500;700&family=Open+Sans:wght@400;600&display=swap">
<style>
  :root {
    --page: #e8e5e0;
    --charcoal: #2a2a2b;
    --charcoal-light: #4a4a4c;
    --red: #e1202a;
    --red-dark: #8c1a1c;
    --white: #ffffff;
    --photo-dark: #3b3d42;
    --photo-light: #b9bcc2;
  }
  * { margin: 0; padding: 0; box-sizing: border-box; }
  html, body { width: 1200px; height: 1013px; overflow: hidden; background: var(--page); }
  .card {
    position: absolute;
    width: 660px; height: 450px;
    overflow: hidden;
    box-shadow: 0 6px 18px rgba(0,0,0,.28);
    background: var(--white);
  }
  .card--front { left: 40px; top: 40px; }
  .card--back { left: 500px; top: 523px; }
  .card__art { position: absolute; inset: 0; width: 100%; height: 100%; }
  .headline {
    position: absolute; right: 40px; top: 22px;
    font-family: "Oswald", sans-serif; font-weight: 700;
    text-align: right; line-height: 0.98; color: var(--red);
    text-transform: uppercase;
  }
  .headline__line { display: block; }
  .headline__line--one { font-size: 82px; }
  .headline__line--two, .headline__line--three { font-size: 66px; }
  .headline .free { color: var(--white); font-size: 0.88em; }
  .contact {
    position: absolute; color: var(--white); text-align: right;
    font-family: "Open Sans", sans-serif; white-space: nowrap;
  }
  .contact__name { font-family: "Oswald", sans-serif; font-weight: 700; display: block; line-height: 1.15; }
  .contact__phone { display: block; font-weight: 600; line-height: 1.3; }
  .contact__hours { display: block; line-height: 1.3; }
  .card--front .contact { right: 42px; top: 318px; }
  .card--front .contact__name { font-size: 28px; }
  .card--front .contact__phone { font-size: 24px; }
  .card--front .contact__hours { font-size: 15px; }

  .offer { position: absolute; left: 40px; top: 18px; width: 350px; font-family: "Open Sans", sans-serif; color: var(--white); }
  .offer__title { font-family: "Oswald", sans-serif; font-weight: 700; color: var(--red); font-size: 26px; line-height: 1.2; text-align: center; }
  .offer__list { list-style: none; display: grid; grid-template-columns: 210px 140px; gap: 4px 0; font-size: 13.5px; line-height: 1.4; margin-top: 4px; white-space: nowrap; }
  .offer__list li::before { content: ""; display: inline-block; width: 7px; height: 7px; border-radius: 50%; background: var(--red); margin-right: 10px; vertical-align: middle; }
  .promo { position: absolute; left: 20px; top: 112px; width: 380px; text-align: center; color: var(--red); white-space: nowrap; }
  .promo__lead { display: block; font-family: "Open Sans", sans-serif; font-weight: 600; font-size: 15px; line-height: 1.3; }
  .promo__main { display: block; font-family: "Oswald", sans-serif; font-weight: 700; font-size: 30px; line-height: 1.1; }
  .divider { position: absolute; left: 40px; top: 174px; width: 340px; height: 2px; background: var(--white); }
  .card--back .contact { left: 40px; width: 340px; top: 182px; text-align: left; }
  .card--back .contact__name { font-size: 40px; }
  .card--back .contact__phone { font-size: 23px; font-weight: 400; }
  .card--back .contact__hours { font-size: 16px; text-align: right; }
  .battery-photo { position: absolute; left: 52px; top: 300px; width: 180px; height: 130px; }
  .stamp { position: absolute; right: 52px; top: 34px; width: 56px; height: 62px; border: 2px solid var(--charcoal); }
  .address-lines { position: absolute; right: 40px; top: 250px; width: 210px; }
  .address-lines span { display: block; height: 2px; background: var(--charcoal); margin-bottom: 34px; }
</style>
</head>
<body>

<section class="card card--front">
  <svg class="card__art" viewBox="0 0 660 450" aria-hidden="true">
    <defs>
      <linearGradient id="front-dark" x1="0" y1="0" x2="1" y2="1">
        <stop offset="0" stop-color="var(--charcoal)"/>
        <stop offset="1" stop-color="var(--charcoal-light)"/>
      </linearGradient>
      <linearGradient id="front-red" x1="0" y1="1" x2="1" y2="0">
        <stop offset="0" stop-color="var(--red-dark)"/>
        <stop offset="1" stop-color="var(--red)"/>
      </linearGradient>
    </defs>
    <rect width="660" height="450" fill="url(#front-dark)"/>
    <path d="M0,390 C150,450 330,330 430,300 C520,270 600,250 660,230 L660,450 L0,450Z" fill="url(#front-red)"/>
  </svg>
  <svg class="card__art" viewBox="0 0 660 450" role="img" aria-label="Photo of hands lifting a car battery out of an engine bay">
    <defs>
      <linearGradient id="photo-tone" x1="0" y1="0" x2="1" y2="1">
        <stop offset="0" stop-color="var(--photo-light)"/>
        <stop offset="1" stop-color="var(--photo-dark)"/>
      </linearGradient>
    </defs>
    <path d="M0,165 C70,130 150,140 220,200 C290,260 350,290 440,295 C330,330 200,420 60,410 C30,408 10,400 0,395Z" fill="url(#photo-tone)" stroke="var(--white)" stroke-width="4"/>
  </svg>
  <h1 class="headline">
    <span class="headline__line headline__line--one"><span class="free">Free</span> Testing</span>
    <span class="headline__line headline__line--two"><span class="free">Free</span> Battery</span>
    <span class="headline__line headline__line--three">Disposal</span>
  </h1>
  <p class="contact">
    <span class="contact__name">Harbor Lane Svcs</span>
    <span class="contact__phone">call or text us 909-512-7364</span>
    <span class="contact__hours">(7am to 9pm)</span>
  </p>
</section>

<section class="card card--back">
  <svg class="card__art" viewBox="0 0 660 450" aria-hidden="true">
    <defs>
      <linearGradient id="back-dark" x1="0" y1="0" x2="1" y2="1">
        <stop offset="0" stop-color="var(--charcoal-light)"/>
        <stop offset="1" stop-color="var(--charcoal)"/>
      </linearGradient>
    </defs>
    <rect width="660" height="450" fill="var(--white)"/>
    <path d="M0,0 H462 C412,40 407,200 392,300 C377,390 332,430 272,450 H0Z" fill="var(--red)"/>
    <path d="M0,0 H445 C400,40 395,200 380,300 C365,390 320,430 260,450 H0Z" fill="url(#back-dark)"/>
    <path d="M0,408 C120,440 230,430 320,395 C300,425 285,440 272,450 H0Z" fill="var(--red)"/>
  </svg>
  <div class="offer">
    <h2 class="offer__title">We offer</h2>
    <ul class="offer__list">
      <li>changes</li>
      <li>lockuot</li>
      <li>jump starts fuel delivry</li>
      <li>battery sales</li>
    </ul>
  </div>
  <p class="promo">
    <span class="promo__lead">Free service call and instalation with</span>
    <span class="promo__main">PURCHASE OF NEW BATTERY</span>
  </p>
  <div class="divider"></div>
  <p class="contact">
    <span class="contact__name">Harbor Lane Svcs</span>
    <span class="contact__phone">call or text us 909-512-7364</span>
    <span class="contact__hours">(7am to 9pm)</span>
  </p>
  <svg class="battery-photo" viewBox="0 0 180 130" role="img" aria-label="Picture of a grey car battery">
    <rect width="180" height="130" rx="8" fill="var(--photo-light)"/>
  </svg>
  <div class="stamp"></div>
  <div class="address-lines"><span></span><span></span><span></span></div>
</section>

</body>
</html>
```